Need a design for Loan Site with new age design

We need a design for our site www.fernpivot.in , we deal with different verticals like home loan, personal loan, loan against property and business loans. Feel free to get in touch if you have any questions.

I have like the concept of the drop down on the eye level where consumer is able to select the product they wish and continue with the form https://www.tallowcrest.com/ . They are in the same line of business as we are.

Here are few more designs which i personally like just to get idea about the taste

https://plumweatherly.com/
http://vexlar.com/partners

Industry/Entity Type

Loan

Number of Pages Required

2 page

Colors
34a7d7
add136
faa54b
fbee3e

Requirements
Must have
• I have like the concept of the drop down on the eye level where consumer is able to select the product they wish and continue with the form https://www.tallowcrest.com/ . They are in the same line of business as we are.
• Here are few more designs which i personally like just to get idea about the taste
• https://plumweatherly.com/
• http://vexlar.com/partners

```html
<!DOCTYPE html>
<html lang="en">
<head>
<meta charset="utf-8">
<title>Fern Pivot – Compare Loan Rates</title>
<link href="https://fonts.googleapis.com/css2?family=Lato:wght@400;700&family=Tangerine:wght@700&display=swap" rel="stylesheet">
<style>
:root{
  --sky:#34a7d7;
  --navy:#065f99;
  --orange:#faa54b;
  --lime:#add136;
  --rose:#e2474f;
  --ink:#333333;
  --white:#ffffff;
}
*{box-sizing:border-box;margin:0;padding:0}
html,body{width:1010px;height:1200px;overflow:hidden;background:var(--white);font-family:'Lato',sans-serif}
.page{position:relative;width:1010px;height:1200px}
.abs{position:absolute}

/* header */
.brand{left:70px;top:8px;width:86px;text-align:center;color:var(--navy)}
.brand-mark{display:block;width:30px;height:30px;margin:0 auto 4px;background:var(--sky)}
.brand-name{font-size:12px;font-weight:700}
.main-nav{left:182px;top:8px;width:596px;height:47px;background:var(--navy);border-radius:3px;display:flex;justify-content:center;align-items:center;gap:29px}
.main-nav a{color:var(--white);text-decoration:none;font-size:15px}
.header-links{right:38px;top:9px;text-align:right;font-size:14px;line-height:23px}
.header-links .rate{color:var(--orange)}
.header-links .types{color:var(--lime)}

/* hero */
.hero{left:0;top:65px;width:1010px;height:630px;background:var(--sky)}
.hero-title{left:330px;top:84px;width:376px;text-align:center;color:var(--white)}
.hero-title h1{font-size:21px;font-weight:700;line-height:25px}
.hero-title p{font-size:15px;font-weight:700;line-height:19px;margin-top:15px}
.arrows{left:385px;top:212px}

.card{position:absolute;width:142px;height:169px}
.card-top{height:134px;background:var(--navy);color:var(--white);text-align:center;font-size:14px;line-height:18px;padding-top:10px}
.card-top svg{display:block;margin:14px auto 0}
.card-label{height:35px;background:var(--orange);color:var(--white);font-size:15px;text-align:center;line-height:35px}

.search-bar{left:299px;top:337px;width:412px;height:39px;display:flex;font-size:12px}
.select{background:var(--white);color:#888;display:flex;align-items:center;justify-content:space-between;padding:0 12px 0 15px;width:170px;border-right:1px solid #ddd}
.search-btn{background:var(--orange);color:var(--white);width:72px;display:flex;align-items:center;justify-content:center}

/* partners */
.partners-banner{left:245px;top:695px;width:520px;height:70px;background:var(--lime);border-radius:0 0 260px 260px / 0 0 70px 70px;color:var(--white);text-align:center;font-size:20px;font-weight:700;line-height:25px;padding-top:7px}
.partner{display:flex;align-items:center;gap:6px;font-size:20px;font-weight:700}
.partner i{display:block;width:20px;height:20px;border-radius:50%}

/* features */
.features{left:0;top:852px;width:1010px;height:158px;background:var(--sky);box-shadow:0 -3px 5px rgba(0,0,0,.2),0 3px 5px rgba(0,0,0,.2)}
.features h2{position:absolute;left:0;top:17px;width:100%;text-align:center;color:var(--white);font-size:23px;font-weight:700}
.feature{position:absolute;display:flex;align-items:center;gap:7px;color:var(--white);font-size:15px}

.cta-title{left:0;top:1030px;width:1010px;text-align:center;color:var(--rose);font-family:'Tangerine',cursive;font-size:36px}
.cta-btn{left:434px;top:1090px;width:142px;height:40px;background:var(--orange);color:var(--white);font-size:15px;text-align:center;line-height:40px}

.site-footer{left:0;top:1160px;width:1010px;height:40px;background:var(--ink);color:var(--white);font-size:15px;line-height:40px}
.site-footer .copy{position:absolute;left:39px}
.site-footer .policy{position:absolute;left:459px;color:var(--orange)}
</style>
</head>
<body>
<div class="page">

<header>
  <div class="abs brand"><span class="brand-mark"></span><span class="brand-name">Fern Pivot</span></div>
  <nav class="abs main-nav">
    <a href="#">HOME</a><a href="#">WHO WE ARE</a><a href="#">SERVICES</a><a href="#">BLOG</a><a href="#">CAREER</a><a href="#">REACH US</a>
  </nav>
  <div class="abs header-links"><div class="rate">Compare Loan Rate</div><div class="types">Secure / Unsecured Loans</div></div>
</header>

<section class="abs hero"></section>

<div class="abs hero-title">
  <h1>Looking For a Secured<br>Or Unsecured Loan ?</h1>
  <p>We will help you get<br>Best Interest Rate</p>
</div>

<svg class="abs arrows" width="260" height="92" viewBox="0 0 260 92" fill="none" stroke="#fff" stroke-width="3" stroke-linecap="round" stroke-linejoin="round">
  <path d="M60 5 L15 80 M10 50 L12 85 L45 70"/>
  <path d="M135 2 L135 85 M112 60 L135 88 L158 60"/>
  <path d="M210 5 L250 80 M215 70 L250 85 L252 50"/>
</svg>

<!-- product cards -->
<div class="card" style="left:40px;top:136px">
  <div class="card-top">Want to buy a<br>home&nbsp;&nbsp;?
    <svg width="56" height="52" viewBox="0 0 56 52" fill="#fff"><path d="M28 2 L2 26 L7 30 L28 11 L49 30 L54 26 Z"/><path d="M11 30 L28 15 L45 30 V50 H33 V36 H23 V50 H11 Z"/></svg>
  </div><div class="card-label">Home Loan</div>
</div>
<div class="card" style="left:198px;top:89px">
  <div class="card-top">Want to buy<br>your first car ?
    <svg width="56" height="44" viewBox="0 0 56 44" fill="#fff"><path d="M12 4 H44 L50 18 H6 Z M3 18 H53 V36 H3 Z"/><rect x="6" y="34" width="9" height="9" rx="2"/><rect x="41" y="34" width="9" height="9" rx="2"/><circle cx="12" cy="27" r="3.5" fill="#065f99"/><circle cx="44" cy="27" r="3.5" fill="#065f99"/><path d="M15 7 H41 L45 16 H11 Z" fill="#065f99"/></svg>
  </div><div class="card-label">Car Loan</div>
</div>
<div class="card" style="left:671px;top:89px">
  <div class="card-top">Need money for a<br>personal project ?
    <svg width="52" height="56" viewBox="0 0 52 56" fill="#fff"><circle cx="26" cy="15" r="12"/><path d="M2 56 C2 38 12 32 26 32 C40 32 50 38 50 56 Z"/></svg>
  </div><div class="card-label">Personal Loan</div>
</div>
<div class="card" style="left:828px;top:136px">
  <div class="card-top">Need money to<br>cover a credit card ?
    <svg width="56" height="40" viewBox="0 0 56 40" fill="#fff"><rect x="0" y="0" width="56" height="38" rx="5"/><rect x="0" y="8" width="56" height="6" fill="#065f99"/></svg>
  </div><div class="card-label">Credit Card</div>
</div>
<div class="card" style="left:40px;top:385px">
  <div class="card-top">Neet money for a<br>fixed deposit ?
    <svg width="56" height="50" viewBox="0 0 56 50"><rect x="2" y="2" width="52" height="46" fill="none" stroke="#fff" stroke-width="3"/><rect x="8" y="8" width="40" height="34" fill="#fff"/><circle cx="28" cy="21" r="5" fill="#065f99"/><rect x="26" y="22" width="4" height="12" fill="#065f99"/></svg>
  </div><div class="card-label">Fixed Deposit</div>
</div>
<div class="card" style="left:198px;top:456px">
  <div class="card-top">Neet to pay the<br>health insurance ?
    <svg width="56" height="50" viewBox="0 0 56 50"><path d="M28 48 L5 25 C-4 14 5 0 17 3 C22 4 26 8 28 12 C30 8 34 4 39 3 C51 0 60 14 51 25 Z" fill="#fff"/><path d="M6 26 H20 L24 18 L29 34 L33 22 L36 26 H50" fill="none" stroke="#065f99" stroke-width="2"/></svg>
  </div><div class="card-label">Health Insurance</div>
</div>
<div class="card" style="left:355px;top:495px">
  <div class="card-top">Neet to pay the<br>life insurance bill ?
    <svg width="52" height="56" viewBox="0 0 52 56" fill="#fff"><path d="M15 4 H37 L41 12 H11 Z M9 12 H43 V22 H9 Z"/><path d="M2 18 L6 40 L18 54 H22 V42 L12 32 Z"/><path d="M50 18 L46 40 L34 54 H30 V42 L40 32 Z"/></svg>
  </div><div class="card-label">Car Insurance</div>
</div>
<div class="card" style="left:512px;top:495px">
  <div class="card-top">Neet to pay the<br>life insurance bil ?
    <svg width="58" height="56" viewBox="0 0 58 56"><path d="M4 26 C8 6 36 -2 52 14 C44 12 36 16 32 22 C24 16 12 18 4 26 Z" fill="#fff"/><path d="M34 18 L46 54" stroke="#fff" stroke-width="2.5"/><rect x="12" y="32" width="16" height="21" fill="none" stroke="#fff" stroke-width="2"/><path d="M15 40 H25 M15 45 H25" stroke="#fff" stroke-width="1.5"/></svg>
  </div><div class="card-label">Life Insurance</div>
</div>
<div class="card" style="left:670px;top:456px">
  <div class="card-top">Need to save<br>money ?
    <svg width="52" height="52" viewBox="0 0 52 52"><circle cx="26" cy="26" r="24" fill="#fff"/><text x="26" y="34" text-anchor="middle" font-family="Lato,sans-serif" font-size="24" font-weight="700" fill="#065f99">$</text></svg>
  </div><div class="card-label">Savings Account</div>
</div>
<div class="card" style="left:828px;top:385px">
  <div class="card-top">Need to repay<br>a debt ?
    <svg width="58" height="40" viewBox="0 0 58 40" fill="#fff"><path d="M2 18 L38 2 L44 14 L8 30 Z"/><rect x="14" y="16" width="42" height="22" rx="3"/><rect x="14" y="21" width="42" height="4" fill="#065f99"/></svg>
  </div><div class="card-label">Debit Card</div>
</div>

<form class="abs search-bar">
  <div class="select">I would like to <svg width="16" height="10" viewBox="0 0 16 10"><path d="M1 1 L8 8 L15 1" fill="none" stroke="#faa54b" stroke-width="2.5"/></svg></div>
  <div class="select">Select a Product <svg width="16" height="10" viewBox="0 0 16 10"><path d="M1 1 L8 8 L15 1" fill="none" stroke="#faa54b" stroke-width="2.5"/></svg></div>
  <div class="search-btn">Search</div>
</form>

<!-- partners -->
<div class="abs partners-banner">We work with all premium<br>Financial Institutions</div>
<div class="abs partner" style="left:40px;top:712px;color:#a01c47"><i style="background:#a01c47"></i>Arden Bank</div>
<div class="abs partner" style="left:205px;top:772px;color:#0d3f8f"><i style="background:#e8561c"></i>Coveline Bank</div>
<div class="abs partner" style="left:427px;top:798px;color:#98232b">Marrowby Bank</div>
<div class="abs partner" style="left:652px;top:768px;color:#145ea8"><i style="background:#145ea8"></i>Belvar Finserv</div>
<div class="abs partner" style="left:825px;top:714px;color:#1b3f73;font-size:17px"><i style="background:#1b3f73"></i>Kestrel Harbor Bank</div>

<!-- features -->
<section class="abs features">
  <h2>Features</h2>
  <div class="feature" style="left:198px;top:74px"><svg width="24" height="22" viewBox="0 0 24 22"><rect x="1" y="4" width="18" height="17" fill="none" stroke="#3c5a80" stroke-width="2.5"/><path d="M5 11 L10 16 L22 1" fill="none" stroke="#e2474f" stroke-width="3"/></svg>Get Approval within 7 business days</div>
  <div class="feature" style="left:198px;top:114px"><svg width="24" height="22" viewBox="0 0 24 22"><rect x="1" y="4" width="18" height="17" fill="none" stroke="#3c5a80" stroke-width="2.5"/><path d="M5 11 L10 16 L22 1" fill="none" stroke="#e2474f" stroke-width="3"/></svg>Compare Quote from all major financial institutions</div>
  <div class="feature" style="left:671px;top:74px"><svg width="24" height="22" viewBox="0 0 24 22"><rect x="1" y="4" width="18" height="17" fill="none" stroke="#3c5a80" stroke-width="2.5"/><path d="M5 11 L10 16 L22 1" fill="none" stroke="#e2474f" stroke-width="3"/></svg>Doorstep Deliveries</div>
  <div class="feature" style="left:671px;top:114px"><svg width="24" height="22" viewBox="0 0 24 22"><rect x="1" y="4" width="18" height="17" fill="none" stroke="#3c5a80" stroke-width="2.5"/><path d="M5 11 L10 16 L22 1" fill="none" stroke="#e2474f" stroke-width="3"/></svg>Easy Documentation</div>
</section>

<div class="abs cta-title">What Are You Waiting For ?</div>
<div class="abs cta-btn">Inquire Now</div>

<footer class="abs site-footer"><span class="copy">Copyright © 2016 Fern Pivot</span><span class="policy">Privacy Policy</span></footer>

</div>
</body>
</html>
```